Kids painting app needs in-app icons

Need a set of in-app icons for a kids painting app. There are currently place-holder icons in place, but these icons are inconsistent and quite dull for a kids app.

Specifically we need 7 icons and a design for a slider.

***********************************************************************************************
See the "Nice to Haves" section below for updated comments to this brief.

We are looking for icons that are playful, but also don't want them to be overbearing, since the intent of the app is to focus on the painting experience itself, so limiting visual clutter is one of the core design goals.

We also want to avoid words as icons, since the intention is to localise the app in to a number of different languages, and we want to avoid the need to localise the icons themselves.

See the attached images for reference to the current placeholder layout. We do not what to spend too much time adjusting the current layout at present, but feel free to play around with your layout when presenting your work in place if you feel it significantly enhances the painting app overall.

You can try out the app on a recent iOS device by signing up to the alpha testing program from our web-site - www.brightdabstudio.com

Regards,
Kim

Target Market(s)

Painting app designed specifically for kids

Colors

Designer to choose colors to be used in the design.

Requirements
Must have
• The required elements are as follows:
• * Clean brush icon
• Tapping this icon will clean the paint off of the brush. This is currently being represented by the head of a brush, which we believe is quite appropriate, but if you feel there is a better way to represent this action we are open to suggestions.
• A design idea may be to have two variations of this icon: one with paint on the brush and one without paint on the brush. It would then be possible to display, or perhaps even blend between these two images to highlight the build up of paint on the brush, but primarily to highlight the purpose of the icon by giving visual feedback after pressing the icon
• * Options icon
• This is currently being represented by a gear icon. The option icon and the clean brush icon are the only two UI elements that are always visible. This icon simply shows / hides the final three additional icons
• * Share icon
• This icon is based on the standard iOS share icon, which launches the standard iOS share dialog. Any suggestions on a more kids friendly design are welcome, but feel free to include a design based off of the standard share icon if you feel it is still the most appropriate icon design to use
• * Return to Gallery
• We are currently using a green tick icon to represent this operation. Some of the thought process behind this icon was that we were also saving the image as we returned to the gallery, however saving will now happen automatically after each brush stroke, so that mental concept has been relaxed.
• * Reset Painting
• We are currently using a red X icon to represent this operation. This allows you to clear the canvas, clean the brush, and reset the paint palette all with a single icon press.
• * Undo / Redo
• While not implemented at present, we may implement undo / redo functionality in the future, so we would like icon designs for these. Also, having to include designs for undo and redo will like influence how you design the Return to Gallery icon, in order to differentiate the operations.
• There is also one more visual element that need further attention, but isn't exactly an icon:
• * Brush width slider
• After performing a long press on the clean brush icon, the brush width slider appears. This is currently using a standard iOS slider. Note that ideally this slider should not always be visible, in order to limit on-screen clutter, but it is also important for it to be easily discoverable and intuitive to use.
• Side note:
• It is straight-forward to tint any white icons inside iOS, so icons can be created in grey scale and coloured inside the app. However, if your design has a specific colour theme please provide both grey scale and full colour versions to make it easy for use to possibly offer different colour themes inside the app at a later date.
Nice to have
• ***********************************************************************************************
• UPDATE: 23 May - Consistency with logo
• Firstly, thank you to everyone who has already submitted a design. Seeing
• the variation in design makes it a lot easier for us to figure out our intended
• direction.
• I have uploaded two additional images of our P logo, and how it is integrated into the Dabwell Kids logo. Also, you may have noticed that the palette is rounded with circular paint swatches.
• We would like this rounded / circular theme to be a part of the icon designs also. This could mean having a rounded / circular background outline or rounded / circular features of the icon itself.
• Having the outline of the icons themselves appearing as if painted is something we are interested in exploring, similar to the P logo itself but probably greyscale or outlined
• Having seen a number of designs we are gravitating towards cleaner designs, either black and white or using just a single colour

```html
<!DOCTYPE html>
<html lang="en">
<head>
<meta charset="utf-8">
<title>Painting Screen Controls</title>
<style>
  :root {
    --canvas: #ffffff;
    --bar: #ffd600;
    --palette: #f08a00;
    --palette-dark: #b85e00;
    --undo: #2e8b0c;
    --swap: #0f7c8a;
    --rotate-back: #0a3aa8;
    --rotate-forward: #8a00b4;
    --share: #c2004f;
    --settings: #4a4a4a;
    --icon: #ffffff;
    --track: #8a8a8a;
  }
  * { box-sizing: border-box; margin: 0; padding: 0; }
  html, body { width: 1200px; height: 900px; overflow: hidden; background: var(--canvas); }
  .painting-screen { position: relative; width: 1200px; height: 900px; }
  .round-button {
    position: absolute;
    width: 76px; height: 76px;
    border-radius: 50%;
    display: flex; align-items: center; justify-content: center;
    box-shadow: 0 4px 6px rgba(0,0,0,0.28), inset 0 -4px 6px rgba(0,0,0,0.25), inset 0 3px 5px rgba(255,255,255,0.25);
  }
  .round-button svg { width: 46px; height: 46px; overflow: visible; }
  .brush-button {
    left: 32px; top: 38px;
    background: radial-gradient(circle at 50% 40%, #ff9a10 55%, var(--palette-dark) 100%);
  }
  .width-slider { position: absolute; left: 66px; top: 144px; width: 4px; height: 154px; background: var(--track); border-radius: 2px; }
  .width-slider .knob {
    position: absolute; left: -8px; top: 21px; width: 20px; height: 20px;
    border-radius: 50%; background: #fff; box-shadow: 0 1px 4px rgba(0,0,0,0.35);
  }
  .tool-bar {
    position: absolute; left: 618px; top: 30px; width: 560px; height: 92px;
    background: var(--bar); border-radius: 46px;
    box-shadow: 0 4px 10px rgba(0,0,0,0.18);
  }
  .tool-bar .round-button { top: 8px; }
  .undo-button { left: 10px; background: radial-gradient(circle at 50% 40%, #3aa012 60%, #1f5e08 100%); }
  .swap-button { left: 110px; background: radial-gradient(circle at 50% 40%, #138e9e 60%, #0a5660 100%); }
  .rotate-back-button { left: 206px; background: radial-gradient(circle at 50% 40%, #0d44c0 60%, #062a7a 100%); }
  .rotate-forward-button { left: 296px; background: radial-gradient(circle at 50% 40%, #9c05cc 60%, #5e0080 100%); }
  .share-button { left: 385px; background: radial-gradient(circle at 50% 40%, #d4065a 60%, #85003a 100%); }
  .settings-button { left: 473px; background: radial-gradient(circle at 50% 40%, #555 60%, #2e2e2e 100%); }
  .stroke-icon { fill: none; stroke: var(--icon); stroke-width: 3.4; stroke-linecap: round; stroke-linejoin: round; }
</style>
</head>
<body>
<main class="painting-screen">
  <div class="round-button brush-button" aria-label="Clean brush">
    <svg viewBox="-23 -23 46 46">
      <path d="M-4 -16 C-17 -16 -21 -4 -19 4 C-17 12 -8 16 2 15 C8 14 7 9 4 7 C1 5 3 1 8 2 C15 3 19 -2 17 -7 C14 -13 6 -16 -4 -16 Z" fill="#ffd35c"/>
      <circle cx="-11" cy="-10" r="3.5" fill="#1d6fd6"/>
      <circle cx="-14" cy="-1" r="3.5" fill="#f08a00"/>
      <circle cx="-11" cy="9" r="3.5" fill="#2fa3e0"/>
      <circle cx="0" cy="13" r="3.5" fill="#e8473c"/>
      <circle cx="12" cy="-4" r="3.5" fill="#e8473c"/>
      <line x1="-3" y1="3" x2="19" y2="-19" stroke="#6b6b6b" stroke-width="2.6" stroke-linecap="round"/>
      <path d="M-5 5 L-1 0 L2 3 Z" fill="#d8325a"/>
    </svg>
  </div>
  <div class="width-slider" aria-label="Brush width"><div class="knob"></div></div>

  <nav class="tool-bar">
    <div class="round-button undo-button" aria-label="Back to gallery">
      <svg viewBox="-23 -23 46 46"><path class="stroke-icon" d="M-12 -6 H6 A7 7 0 0 1 6 8 H-10 M-6 -12 L-12 -6 L-6 0"/></svg>
    </div>
    <div class="round-button swap-button" aria-label="Reset painting">
      <svg viewBox="-23 -23 46 46">
        <path fill="var(--icon)" d="M-4 -15 C-10 -12 -10 -6 -8 -2 L-12 -2 L-6 6 L0 -2 L-4 -2 C-6 -6 -6 -11 -4 -15 Z"/>
        <path fill="var(--icon)" d="M4 15 C10 12 10 6 8 2 L12 2 L6 -6 L0 2 L4 2 C6 6 6 11 4 15 Z"/>
      </svg>
    </div>
    <div class="round-button rotate-back-button" aria-label="Undo">
      <svg viewBox="-23 -23 46 46">
        <path class="stroke-icon" d="M-12 0 A13 13 0 0 1 12 -4"/>
        <path class="stroke-icon" d="M12 -4 A13 13 0 0 1 -12 4" stroke-dasharray="4 5"/>
        <path class="stroke-icon" d="M-17 -5 L-12 1 L-6 -4"/>
      </svg>
    </div>
    <div class="round-button rotate-forward-button" aria-label="Redo">
      <svg viewBox="-23 -23 46 46">
        <path class="stroke-icon" d="M-12 -4 A13 13 0 0 1 12 0"/>
        <path class="stroke-icon" d="M-12 -4 A13 13 0 0 0 12 4" stroke-dasharray="4 5"/>
        <path class="stroke-icon" d="M17 -5 L12 1 L6 -4"/>
      </svg>
    </div>
    <div class="round-button share-button" aria-label="Share">
      <svg viewBox="-23 -23 46 46">
        <line class="stroke-icon" x1="-9" y1="0" x2="9" y2="-10"/>
        <line class="stroke-icon" x1="-9" y1="0" x2="9" y2="10"/>
        <circle class="stroke-icon" cx="-10" cy="0" r="5" fill="var(--share)"/>
        <circle class="stroke-icon" cx="10" cy="-11" r="5" fill="var(--share)"/>
        <circle class="stroke-icon" cx="10" cy="11" r="5" fill="var(--share)"/>
      </svg>
    </div>
    <div class="round-button settings-button" aria-label="Options">
      <svg viewBox="-23 -23 46 46">
        <circle cx="0" cy="0" r="15" fill="none" stroke="var(--icon)" stroke-width="7" stroke-dasharray="5.9 5.9"/>
        <circle cx="0" cy="0" r="13" fill="var(--icon)"/>
        <circle cx="0" cy="0" r="5" fill="var(--settings)"/>
      </svg>
    </div>
  </nav>
</main>
</body>
</html>
```